High End Personalized Functional Medicine in Women's Health

We are adding new and exciting personalized medicine services to our Women's Health Care practice focusing on health optimization and anti-aging as well as hormone replacement therapy and need a high end brochure to educate patients about these services. We would like to see a zen-like design that has feminine appeal. Our office colors are vibrant but soothing. We have utilized the concepts of feng shui to optimize our positive energy. The exterior of the building is peach and cream and these colors would blend with that energy The final design should communicate a sense that you can take control of your health and aging.
Updates

Target Market(s)

Females age 35-65 with annual income >$75000/year

Industry/Entity Type

Health And Wellness

Logo Text

Bright Path is the company name. Our sister company is Mesa Rio Ob/Gyn

Font styles to use
Serif

Colors

Designer to choose colors to be used in the design.

Requirements
Must have
• My project must have clean lines. I like a strong feminine appearance, not a fluffy curvy feminine look. Professional appearance, Brochure would be on thicker card stock. A strong front page that makes you want to open the brochure
Nice to have
• Eye catching photos that complement our message . I am not tied to the peach and cream color recommendation, but find those colors feminine but not so cliche as pinks and purples.
Should not have
• frilly design

```html
<!DOCTYPE html>
<html lang="en">
<head>
<meta charset="utf-8">
<title>Time to Balance Your Hormones – Brochure Inside Spread</title>
<link rel="stylesheet" href="https://fonts.googleapis.com/css2?family=EB+Garamond:wght@400;500;600&family=Arimo:wght@700&display=swap">
<style>
  :root {
    --backdrop: #9a9a9c;
    --cream: #f7f4df;
    --green: #35973d;
    --green-dark: #2a7f31;
    --gold: #d89b1f;
    --band-gold: #d4a41c;
    --ink: #2f2f2a;
    --white: #ffffff;
  }
  * { margin: 0; padding: 0; box-sizing: border-box; }
  html, body { width: 1200px; height: 800px; overflow: hidden; }
  body { background: var(--backdrop); position: relative; font-family: "EB Garamond", Georgia, serif; color: var(--ink); }

  .brochure {
    position: absolute; left: 45px; top: 50px; width: 1110px; height: 700px;
    background: var(--cream); overflow: hidden;
    box-shadow: 0 18px 40px rgba(0,0,0,.25);
  }
  .band-top { position: absolute; left: 0; top: 0; width: 100%; height: 14px; background: var(--green); }
  .band-bottom { position: absolute; left: 0; bottom: 0; width: 100%; height: 10px; background: var(--band-gold); }
  .fold { position: absolute; top: 0; width: 2px; height: 100%; background: linear-gradient(90deg, rgba(0,0,0,.08), rgba(255,255,255,.3)); z-index: 5; }
  .fold--one { left: 369px; }
  .fold--two { left: 739px; }

  .block { position: absolute; }
  .panel-title { font-weight: 600; color: var(--green-dark); font-size: 20px; text-decoration: underline; text-underline-offset: 3px; line-height: 1.1; }
  .panel-title--plain { text-decoration: none; }
  .topic { font-weight: 600; color: var(--gold); font-size: 18px; line-height: 1.1; }
  .copy { font-size: 12.2px; line-height: 1.32; text-align: justify; }

  .photo { position: absolute; display: block; }

  .promo {
    position: absolute; left: 370px; top: 228px; width: 272px; height: 300px;
    background: var(--green); padding: 34px 0 0 30px;
  }
  .promo-text { font-family: "Arimo", Arial, sans-serif; font-weight: 700; color: var(--white); font-size: 33px; line-height: 1.22; letter-spacing: .5px; }
</style>
</head>
<body>
<div class="brochure">
  <div class="band-top"></div>
  <div class="band-bottom"></div>
  <div class="fold fold--one"></div>
  <div class="fold fold--two"></div>

  <!-- Panel 1: symptoms -->
  <h2 class="block panel-title" style="left:28px; top:26px;">What Symptoms Do We Treat?</h2>
  <h3 class="block topic" style="left:28px; top:60px;">Weight gain</h3>
  <p class="block copy" style="left:28px; top:84px; width:314px;">Adrenal dysfunction results in cortisol imbalance. The major function of cortisol is to help balance blood sugar. When cortisol is out of balance, your body will store body fat rather than burning fat for fuel resulting in weight gain. Menopausal hormone imbalance will also result in abdominal weight gain.</p>

  <svg class="photo" style="left:0; top:200px;" width="370" height="225" viewBox="0 0 370 225" role="img" aria-label="Photo of a woman measuring her waist with a tape measure">
    <defs><linearGradient id="waistTone" x1="0" y1="0" x2="0" y2="1"><stop offset="0" stop-color="#eef0f2"/><stop offset=".5" stop-color="#e2c2ad"/><stop offset="1" stop-color="#3f5f8c"/></linearGradient></defs>
    <path d="M0 18 Q185 -8 370 12 L370 198 Q185 226 0 206 Z" fill="url(#waistTone)"/>
  </svg>

  <h3 class="block topic" style="left:28px; top:442px;">Fatigue</h3>
  <p class="block copy" style="left:28px; top:466px; width:314px;">Adrenal exhaustion results from long term stress that depletes cortisol. Testing and correcting cortisol will improve energy levels. Long term stress can result in mitochondrial dysfunction and organic acid tests can tell us how to support your mitochondria.</p>

  <svg class="photo" style="left:0; top:540px;" width="370" height="150" viewBox="0 0 370 150" role="img" aria-label="Photo of a tired woman resting her head on a desk beside a mug">
    <defs><linearGradient id="fatigueTone" x1="0" y1="0" x2="1" y2="1"><stop offset="0" stop-color="#b9cbd2"/><stop offset=".5" stop-color="#c9b29a"/><stop offset="1" stop-color="#e6e3dc"/></linearGradient></defs>
    <path d="M0 14 Q185 -6 370 8 L370 150 L0 150 Z" fill="url(#fatigueTone)"/>
  </svg>

  <!-- Panel 2: conditions and message -->
  <h3 class="block topic" style="left:398px; top:26px;">Depression</h3>
  <p class="block copy" style="left:398px; top:50px; width:314px;">We focus both on cortisol and the brain neurotransmitters dopamine, epinephrine and norepinephrine to evaluate causes of depression. Hormone imbalance can also result in both anxiety and depression.</p>
  <h3 class="block topic" style="left:398px; top:122px;">Female Hormone Imbalance</h3>
  <p class="block copy" style="left:398px; top:146px; width:314px;">Optimizing hormonal balance is our specialty. We focus on optimizing hormone levels with bio-identical hormones, but also know that adrenal treatment protocols can improve symptoms of hot flashes, night sweats, and foggy thinking.</p>

  <div class="promo">
    <p class="promo-text">TIME TO<br>BALANCE<br>YOUR<br>HORMONES</p>
  </div>

  <svg class="photo" style="left:642px; top:150px;" width="468" height="378" viewBox="0 0 468 378" role="img" aria-label="Photo of a woman in white holding a yoga balance pose in a flowering meadow under a pale sky">
    <defs><linearGradient id="meadowTone" x1="0" y1="0" x2="0" y2="1"><stop offset="0" stop-color="#a9c6dc"/><stop offset=".6" stop-color="#dfe9ee"/><stop offset=".8" stop-color="#8fae4a"/><stop offset="1" stop-color="#4f7a2a"/></linearGradient></defs>
    <path d="M0 78 L98 78 Q260 4 468 18 L468 300 Q300 300 160 378 L0 378 Z" fill="url(#meadowTone)"/>
  </svg>

  <h3 class="block topic" style="left:398px; top:546px;">GI problems</h3>
  <p class="block copy" style="left:398px; top:570px; width:314px;">The immune cells that line our digestive tract are regulated by cortisol. Cortisol imbalance results in inflammation and “leaky gut” causing digestive symptoms like bloating, heartburn, constipation, or diarrhea. Utilizing a comprehensive program that includes avoiding inflammatory foods and GI Vista stool testing allow us to find underlying infections or sources of inflammation and allow us to develop a focused treatment plan.</p>

  <!-- Panel 3: visit and protocols -->
  <h2 class="block panel-title" style="left:766px; top:26px;">What can I expect from my first visit?</h2>
  <p class="block copy" style="left:766px; top:56px; width:316px;">During your initial consultation, we want to get to know each other and find out your expectations for health. We will explore your health history and symptoms as well as lifestyle factors including diet and sleep. We will discuss your goals and reasons for getting healthy. We know that we must incorporate lifestyle changes including stress reduction, diet and exercise optimization in any program for healing. We will discuss testing recommendations including blood work, hormone evaluation, cortisol, GI, and organic acid tests as well as nutritional and personal coaching options.</p>

  <h2 class="block panel-title panel-title--plain" style="left:766px; top:470px;">What are your<br>treatment protocols based on?</h2>
  <p class="block copy" style="left:766px; top:520px; width:316px;">Treatment protocols are based on making you feel better with a focused wellness program that treats underlying cause. We want to optimize body systems by reducing inflammation, treating insulin resistance, improving catabolic physiology, and reducing oxidative stress. Treatment protocols are a combination of supplement support and hormone balance in addition to lifestyle optimization. Supplement programs tend to be focused and last approximately 6 months. Hormone programs continue for as long as you have symptoms. We will work together to determine what type of treatment program works best for you.</p>
</div>
</body>
</html>
```